Kestrow - Business Card Design

Design a modern masculine business card for our business

Target Market(s)

Private Market

Industry/Entity Type

Construction

Contact Information for Business Card

Company Name - Name of Person - Address - email address - contact number

Font styles to use
Serif
Sans Serif

Colors
0094D4
00A9DD
6FCCEA
C7EBF8
E9F6FB
00AB8E
00BBA5
67D7C9
C6EFE9
E9F9F6
F0912C
F2A743
F7CA91
FBE8D2
FDF5EE

Requirements
Must have
• Use company logo provided
Nice to have
• Company Logo

```html
<!DOCTYPE html>
<html lang="en">
<head>
<meta charset="utf-8">
<title>Kestrow Construction – Business Card</title>
<link href="https://fonts.googleapis.com/css2?family=Figtree:wght@400;600;800&display=swap" rel="stylesheet">
<style>
  :root {
    --backdrop: #e3e3e3;
    --card-dark: #060809;
    --card-light: #f0f0f0;
    --ink: #1c1c1c;
    --accent: #e5622a;
    --white: #f4f4f4;
  }
  * { margin: 0; padding: 0; box-sizing: border-box; }
  html, body {
    width: 1200px; height: 1200px; overflow: hidden;
    background: var(--backdrop);
    font-family: "Figtree", Arial, sans-serif;
  }
  .stage { position: relative; width: 1200px; height: 1200px; }
  .card {
    position: absolute; left: 234px; width: 731px; height: 418px;
  }
  .card-front { top: 160px; background: var(--card-dark); }
  .card-back { top: 632px; background: var(--card-light); color: var(--ink); }

  .wordmark {
    display: flex; align-items: center; gap: 12px;
    font-weight: 800; text-transform: uppercase; letter-spacing: 0.02em;
    white-space: nowrap;
  }
  .wordmark-square { width: 14px; height: 14px; background: var(--accent); flex: none; }
  .front-mark {
    position: absolute; left: 0; right: 0; top: 185px;
    justify-content: center; color: var(--white); font-size: 32px;
  }

  .person-name {
    position: absolute; left: 64px; top: 64px;
    font-size: 33px; font-weight: 600; color: var(--accent);
    white-space: nowrap;
  }
  .person-role {
    position: absolute; left: 65px; top: 104px;
    font-size: 19px; font-weight: 400;
  }
  .divider {
    position: absolute; left: 64px; top: 139px; width: 597px; height: 2px;
    background: var(--ink);
  }
  .address {
    position: absolute; left: 64px; top: 236px;
    font-size: 19px; line-height: 26px; font-style: normal;
  }
  .contact-list { position: absolute; left: 64px; top: 298px; list-style: none; }
  .contact-item {
    display: flex; align-items: center; gap: 10px;
    font-size: 19px; line-height: 28px; white-space: nowrap;
  }
  .contact-icon { width: 16px; height: 16px; flex: none; }
  .back-mark {
    position: absolute; right: 70px; top: 302px;
    color: var(--card-dark); font-size: 16px;
  }
</style>
</head>
<body>
<main class="stage">
  <section class="card card-front">
    <div class="wordmark front-mark">
      <span class="wordmark-square"></span>
      <span>Kestrow Construction, Inc</span>
    </div>
  </section>

  <section class="card card-back">
    <h1 class="person-name">Marcus Kestrow</h1>
    <p class="person-role">President</p>
    <div class="divider"></div>

    <address class="address">4170 Ardent Road<br>Fenwick Lake Maine 04712</address>

    <ul class="contact-list">
      <li class="contact-item">
        <svg class="contact-icon" viewBox="0 0 16 16" aria-hidden="true">
          <path fill="var(--accent)" d="M3.6 1.5l2.3 2.6-1.3 1.6c.8 1.9 2.2 3.3 4.1 4.2l1.6-1.3 2.6 2.3-1.2 2.4C6.5 13.4 2.6 9.5 1.2 4.3z"/>
          <path fill="none" stroke="var(--accent)" stroke-width="1.3" d="M9 3.2a4 4 0 0 1 3.8 3.8M9 .9a6.3 6.3 0 0 1 6.1 6.1"/>
        </svg>
        <span>(405)-555-0142</span>
      </li>
      <li class="contact-item">
        <svg class="contact-icon" viewBox="0 0 16 16" aria-hidden="true">
          <rect x="0.5" y="3" width="15" height="11" fill="var(--accent)"/>
          <path d="M1 3.6l7 5.2 7-5.2" fill="none" stroke="var(--card-light)" stroke-width="1.3"/>
        </svg>
        <span>services@marcuskestrow.com</span>
      </li>
    </ul>

    <div class="wordmark back-mark">
      <span class="wordmark-square"></span>
      <span>Kestrow Construction, Inc</span>
    </div>
  </section>
</main>
</body>
</html>
```